Flyer design for the Harvest Lantern Summit 2019 (HALSUM)

Design a flyer for our annual conference with basic information about the conference: conference logo and year, Conference name: Harvest Lantern Summit Location: Talbot Community Center (Downtown Portland)482 Wexley Street, Portland, ME 04109, Date: August 8th, 9th, 10th and 11th, 2019Start time 7:00PMI would like the following three words added to the flyer. These words describe the vision of the conference: Prophetic, Fire, Overflow,

Contact info:
Website: www.vostel.org
Phone: 207 555 3184
Email: contact@meadowcrest.org

Target Market(s)

Young adults living in the United States

Industry/Entity Type

Religious

Font styles to use
Sans Serif

Colors

Designer to choose colors to be used in the design.

Requirements
Must have
• HALSUM must logo standout, the reader should be able to take a quick look and find key info,
Should not have
• Cross image, church image

```html
<!DOCTYPE html>
<html lang="en">
<head>
<meta charset="utf-8">
<title>Harvest Lantern Summit 2019 — Flyer</title>
<link rel="stylesheet" href="https://fonts.googleapis.com/css2?family=Arimo:wght@400;700&family=Montserrat:wght@700;800&display=swap">
<style>
  :root {
    --backdrop: #bfbebe;
    --paper: #ffffff;
    --flame-orange: #f7931e;
    --summit-blue: #0b75bb;
    --headline-font: "Montserrat", Arial, sans-serif;
    --body-font: "Arimo", Arial, sans-serif;
  }
  html, body {
    margin: 0;
    padding: 0;
    width: 960px;
    height: 1200px;
    overflow: hidden;
    background: var(--backdrop);
  }
  .flyer {
    position: absolute;
    left: 98px;
    top: 60px;
    width: 764px;
    height: 1080px;
    background: var(--paper);
  }
  .flyer svg { display: block; width: 100%; height: 100%; }
  .brand-name { font-family: var(--headline-font); font-weight: 800; font-size: 96px; fill: var(--summit-blue); }
  .brand-year { font-family: var(--headline-font); font-weight: 700; font-size: 40px; fill: var(--flame-orange); letter-spacing: 26px; }
  .brand-rule, .info-rule { stroke: var(--flame-orange); }
  .theme-band { fill: var(--flame-orange); }
  .theme-generation { font-family: var(--headline-font); font-weight: 800; font-size: 98px; fill: var(--paper); }
  .theme-on-fire { font-family: var(--headline-font); font-weight: 800; font-size: 98px; fill: var(--flame-orange); }
  .venue-text, .schedule-text { font-family: var(--body-font); font-weight: 400; font-size: 23px; fill: var(--flame-orange); }
  .pin-outline { fill: none; stroke: var(--summit-blue); stroke-width: 4; }
  .pin-dot { fill: var(--summit-blue); }
  .vision-band { fill: var(--summit-blue); }
  .vision-words { font-family: var(--body-font); font-weight: 700; font-size: 47px; fill: var(--paper); }
</style>
</head>
<body>
  <main class="flyer">
    <svg viewBox="0 0 954 1350" xmlns="http://www.w3.org/2000/svg" aria-labelledby="flyer-title">
      <title id="flyer-title">Harvest Lantern Summit 2019 flyer</title>

      <g class="brand">
        <text class="brand-name" x="90" y="184" textLength="420" lengthAdjust="spacingAndGlyphs">HALSUM</text>
        <line class="brand-rule" x1="90" y1="214" x2="195" y2="214" stroke-width="4"/>
        <text class="brand-year" x="206" y="228">2019</text>
        <line class="brand-rule" x1="407" y1="214" x2="509" y2="214" stroke-width="4"/>
      </g>

      <g class="theme">
        <polygon class="theme-band" points="0,725 590,280 662,380 0,880"/>
        <polygon class="theme-band" points="851,203 954,125 954,280 924,303"/>
        <text class="theme-generation" transform="translate(72 775) rotate(-37)" textLength="685" lengthAdjust="spacingAndGlyphs">GENERATION</text>
        <text class="theme-on-fire" transform="translate(557 540) rotate(-37)" textLength="410" lengthAdjust="spacingAndGlyphs">ON FIRE</text>
      </g>

      <g class="venue">
        <line class="info-rule" x1="331" y1="775" x2="910" y2="775" stroke-width="6"/>
        <g class="pin-icon" transform="translate(380 865)">
          <path class="pin-outline" d="M0 57 L-36 14 A42 42 0 1 1 36 14 Z"/>
          <circle class="pin-dot" cx="0" cy="-12" r="27"/>
        </g>
        <text class="venue-text" x="458" y="845">talbot community center</text>
        <text class="venue-text" x="458" y="875">(downtown portland)482 wexley street,</text>
        <text class="venue-text" x="458" y="904">portland, me 04109</text>
        <line class="info-rule" x1="174" y1="957" x2="910" y2="957" stroke-width="6"/>
      </g>

      <g class="schedule">
        <text class="schedule-text" x="455" y="1011">Date: August 8th, 9th, 10th and 11th, 2019</text>
        <text class="schedule-text" x="455" y="1052">Start time 7:00PM</text>
      </g>

      <g class="vision">
        <rect class="vision-band" x="0" y="1170" width="954" height="85"/>
        <text class="vision-words" x="477" y="1228" text-anchor="middle">PROPHETIC, FIRE, OVERFLOW</text>
      </g>
    </svg>
  </main>
</body>
</html>
```